Quelmar Nutraceuticals Product Label

Quelmar corporation (kel-mar - "to yourhealth") is a healthcare and wellness company in Los Angeles. We produce a line of vitamins/nutritional supplements under brand name KelStrida ( to your progress) and a line of skincare products or creams under the brand name KelSonja ( to your dreams). We already have logos designed for quelmar, kelsonja, and kelstrida which are very similar, and our products can be found in brimtrove.com under these brands as well as at www.drpetravik.com, www.quelmar.com. Our tag line has been "vigour by method"
I am looking to recreate a branding look for our vitamins which can make them appear more vibrant and modern and exciting , while maintaining the air of scientific authority we aimed at before. We want to be able to extend the format to our skin- care line in the future . The skin care line will be sold in upscale stores around the world as well as on the web.
This project requires a new design label for our vitamin products. I will attach appropriate logo files and photos of our vitamins as they are now. They come in white vitamin bottles. The Label wraps around the bottle. The center panel includes the artwork and logos and is bordered on left and right by panels that carry product information. Files attached are self-explanatory. Please email me if you need more direction or info.

```html
<!DOCTYPE html>
<html lang="en">
<head>
<meta charset="utf-8">
<title>KelStrida Supplement Labels</title>
<link rel="stylesheet" href="https://fonts.googleapis.com/css2?family=Oswald:wght@400;500;600;700&family=PT+Serif&family=Roboto:wght@400;500&display=swap">
<style>
  :root {
    --canvas: #eceaea;
    --label: #ffffff;
    --ink: #1b1b1b;
    --ink-soft: #3a3a3a;
    --brand-teal: #1d6f93;
    --accent-pink: #d6246a;
    --accent-gold: #b3892a;
    --gold-light: #d9b24e;
    --band-grey: #8f8f8f;
    --dots: #d4d4d4;
  }
  * { box-sizing: border-box; margin: 0; padding: 0; }
  html, body { width: 1200px; height: 1006px; overflow: hidden; }
  body { background: var(--canvas); position: relative; font-family: "PT Serif", serif; color: var(--ink); }

  .label {
    position: absolute; top: 330px; width: 420px; height: 560px;
    background: var(--label);
    box-shadow: 0 2px 10px rgba(0,0,0,0.08);
    overflow: hidden;
  }
  .label--multi { left: 120px; }
  .label--omega { left: 660px; }

  .dot-field {
    position: absolute; right: 0; top: 20px; width: 230px; height: 190px;
    background: radial-gradient(ellipse at 70% 40%, var(--dots), rgba(255,255,255,0) 70%);
  }

  .brand {
    position: absolute; top: 140px; left: 0; width: 100%;
    display: flex; justify-content: center; align-items: center; gap: 8px;
  }
  .brand__dot { width: 12px; height: 12px; border-radius: 50%; background: var(--brand-teal); }
  .brand__name {
    font-family: "Oswald", sans-serif; font-weight: 500; font-size: 30px;
    letter-spacing: 1px; color: var(--brand-teal);
  }
  .tagline {
    position: absolute; top: 184px; left: 0; width: 100%; text-align: center;
    font-family: "Roboto", sans-serif; font-size: 9px; letter-spacing: 1.5px;
    text-transform: uppercase; color: var(--ink-soft);
  }

  .title {
    position: absolute; left: 0; width: 100%; text-align: center;
    font-family: "Oswald", sans-serif; font-weight: 700; line-height: 1;
    transform-origin: center; color: var(--ink);
  }
  .title--small { top: 222px; font-size: 34px; }
  .title--large { top: 258px; font-size: 46px; letter-spacing: -0.5px; }
  .label--omega .title--small { top: 224px; font-size: 26px; font-weight: 600; }
  .label--omega .title--large { top: 252px; font-size: 52px; }

  .info {
    position: absolute; left: 40px; right: 30px;
    font-size: 22px; line-height: 1.2; color: var(--ink-soft);
  }
  .label--omega .info { left: 60px; }
  .info--ingredients { top: 320px; }
  .info--kind { top: 410px; }
  .info--sub { top: 318px; text-align: center; left: 20px; right: 20px; font-size: 20px; }
  .info--fish { top: 362px; }
  .info--dose { top: 410px; }

  .rule { position: absolute; height: 3px; border-radius: 2px; }
  .rule--pink { top: 384px; left: 40px; width: 300px; background: var(--accent-pink); }
  .rule--gold { top: 394px; left: 60px; width: 250px; background: linear-gradient(90deg, var(--accent-gold), #4a3510); }

  .count-band {
    position: absolute; top: 456px; left: 30px; width: 260px; height: 40px;
    background: linear-gradient(90deg, var(--band-grey), rgba(143,143,143,0));
    padding-left: 12px; display: flex; align-items: center; gap: 8px; color: #ffffff;
  }
  .label--omega .count-band { left: 50px; }
  .count-band__num { font-family: "Roboto", sans-serif; font-size: 30px; }
  .count-band__unit { font-family: "Roboto", sans-serif; font-size: 19px; }

  .ribbon {
    position: absolute; left: 22px; top: 80px; width: 46px; height: 240px;
  }
  .ribbon__text {
    position: absolute; left: 22px; top: 80px; width: 46px; height: 220px;
    display: flex; align-items: center; justify-content: center;
    writing-mode: vertical-rl; transform: rotate(180deg);
    font-family: "Roboto", sans-serif; font-size: 17px; letter-spacing: 2px; color: #ffffff;
  }
</style>
</head>
<body>

  <section class="label label--multi">
    <div class="dot-field" role="img" aria-label="Soft grey halftone dot pattern"></div>
    <div class="brand"><span class="brand__dot"></span><span class="brand__name">KelStrida</span></div>
    <p class="tagline">vigour by method</p>
    <h1 class="title title--small">active</h1>
    <h2 class="title title--large">Woman´s Multi</h2>
    <p class="info info--ingredients">With Soy, Lutein,<br>Black Cohosh and Cranberry</p>
    <div class="rule rule--pink"></div>
    <p class="info info--kind">Dietary Supplement</p>
    <div class="count-band"><span class="count-band__num">90</span><span class="count-band__unit">Tablets</span></div>
  </section>

  <section class="label label--omega">
    <div class="dot-field" role="img" aria-label="Soft grey halftone dot pattern"></div>
    <svg class="ribbon" viewBox="0 0 46 240" aria-hidden="true">
      <defs>
        <linearGradient id="goldRibbon" x1="0" x2="1">
          <stop offset="0" stop-color="#9c7320"/>
          <stop offset="0.5" stop-color="#d9b24e"/>
          <stop offset="1" stop-color="#9c7320"/>
        </linearGradient>
      </defs>
      <path d="M0 0 H46 V240 L23 222 L0 240 Z" fill="url(#goldRibbon)"/>
      <rect x="4" y="4" width="38" height="212" fill="none" stroke="#f3dc93" stroke-width="1"/>
    </svg>
    <span class="ribbon__text">CONCENTRATED</span>
    <div class="brand"><span class="brand__dot"></span><span class="brand__name">KelStrida</span></div>
    <p class="tagline">vigour by method</p>
    <h1 class="title title--small">High Potency</h1>
    <h2 class="title title--large">Omega-3</h2>
    <p class="info info--sub">(polyunsaturated fatty acids)</p>
    <p class="info info--fish">Fish Oil Supplement</p>
    <div class="rule rule--gold"></div>
    <p class="info info--dose">One Softgel Daily</p>
    <div class="count-band"><span class="count-band__num">60</span><span class="count-band__unit">Softgels</span></div>
  </section>

</body>
</html>
```